Powerpoint: Supplemental Presentation Refresh Ideas

Hello! Our quarterly supplemental and investor presentation reports are in powerpoint. They provide a lot of data - tables, charts and graphs. They are in need of some visual updating.
Our challenge is that our in-house team updates the presentations until the very last minute. We need a template they can manipulate. I'm simply looking for some ideas to help refresh the tired presentations.
Here are some links to examples..... you can also find more here: http://ir.vornahold.com/Presentations
http://ir.vornahold.com/Cache/IRCache/30651d71-8f14-050b-e87a-7de361f5d4f7.PDF?O=PDF&T=&Y=&D=&FID=30651d71-8f14-050b-e87a-7de361f5d4f7&iid=102970
http://ir.vornahold.com/Cache/IRCache/714c2e37-4280-50af-5a3f-c28f3ec702df.PDF?O=PDF&T=&Y=&D=&FID=714c2e37-4280-50af-5a3f-c28f3ec702df&iid=102970
http://ir.vornahold.com/Cache/IRCache/5e371c97-e607-4a1f-d889-77c9acae26e6.PDF?O=PDF&T=&Y=&D=&FID=5e371c97-e607-4a1f-d889-77c9acae26e6&iid=102970
Analysts

```html
<!DOCTYPE html>
<html lang="en">
<head>
<meta charset="utf-8">
<title>Supplemental Presentation Template</title>
<link href="https://fonts.googleapis.com/css2?family=Open+Sans:wght@400;600;700&display=swap" rel="stylesheet">
<style>
:root{
  --navy:#1f3a7a;
  --navy-deep:#172c5e;
  --blue:#2e6db5;
  --sky:#5ba3d9;
  --pale:#a9c4e8;
  --ice:#dde6f3;
  --ink:#222;
  --grey:#e6e6e6;
  --grey-dark:#9a9a9a;
  --black:#111;
  --green:#1fb24a;
  --yellow:#f4e61c;
  --amber:#f5b21b;
  --red:#e8141b;
}
*{box-sizing:border-box;margin:0;padding:0}
html,body{width:900px;height:1200px;overflow:hidden;background:#fff}
body{position:relative;font-family:"Open Sans",Arial,sans-serif;color:var(--ink)}
.slide{position:absolute;width:197px;height:152px;background:#fff;overflow:hidden;box-shadow:0 3px 10px rgba(0,0,0,.22)}
.slide.dark{background:var(--navy)}
.slide-title{position:absolute;left:11px;top:9px;font-size:5.4px;font-weight:700;color:var(--navy);text-transform:uppercase;letter-spacing:.1px}
.slide-sub{position:absolute;left:11px;top:17px;font-size:2.5px;color:#333;text-transform:uppercase}
.brand{position:absolute;right:8px;top:5px;display:flex;align-items:center;gap:1.5px}
.brand-dot{width:8px;height:8px;border-radius:50%;background:var(--navy)}
.brand-name{font-size:4px;font-weight:700;color:var(--navy)}
.footer{position:absolute;left:9px;right:9px;bottom:6px;border-top:.5px solid #bbb;font-size:1.8px;color:#999;padding-top:2px;display:flex;justify-content:space-between}
.footer span:first-child{margin-left:82px}
.photo{position:absolute}
.copy{font-size:2.3px;line-height:3.4px;color:#333;text-align:justify}
.copy b{font-weight:700}
.abs{position:absolute}
svg{display:block}
/* cover */
.cover-photo{left:0;top:0;width:197px;height:152px;background:linear-gradient(180deg,#3f6aa8 0%,#6f8fba 40%,#5e6a63 70%,#4e7a38 100%)}
.cover-band{position:absolute;background:rgba(91,163,217,.55);width:8px;height:240px;transform-origin:top left}
.cover-diamond{position:absolute;left:40px;top:-30px;width:160px;height:160px;background:rgba(31,58,122,.82);transform:rotate(45deg);transform-origin:center}
.cover-brand{position:absolute;left:102px;top:48px;font-size:9px;font-weight:700;color:#fff}
.cover-brand::before{content:"";display:inline-block;width:7px;height:7px;background:#fff;margin-right:3px}
.cover-title{position:absolute;left:60px;top:78px;width:130px;text-align:center;color:#fff;font-weight:700;font-size:6px;line-height:8.5px}
.cover-title small{display:block;font-size:3.6px;line-height:6px}
/* agenda */
.agenda-item{position:absolute;left:98px;width:88px;height:11px;background:var(--grey);border-radius:2px;padding:2px 0 0 17px;font-size:2.3px;line-height:2.8px;color:#333}
.agenda-item i{position:absolute;left:-4px;top:-1px;width:12px;height:12px;background:var(--navy);transform:rotate(45deg);font-style:normal}
.agenda-item i::after{content:"";position:absolute;left:4px;top:4px;width:4px;height:4px;background:#fff;border-radius:50%}
.agenda-item small{display:block;font-size:1.6px;color:#777}
.legal{font-size:1.6px;line-height:2.15px;color:#333;text-align:justify}
.legal b{color:var(--navy);font-weight:600}
/* about */
.about-title{position:absolute;left:11px;top:46px;font-size:13px;line-height:13px;color:#fff;font-weight:400}
.about-tag{position:absolute;left:11px;top:75px;font-size:3px;color:#fff;font-weight:600}
.about-copy{position:absolute;left:11px;top:82px;width:77px;color:#fff}
.about-copy p{font-size:2px;line-height:2.8px;margin-bottom:3px;text-align:justify}
.about-photo{left:95px;top:0;width:102px;height:152px;background:linear-gradient(180deg,#6b84a8,#a59a86 50%,#6a5b47);clip-path:polygon(30% 0,100% 0,100% 100%,0 100%,0 70%)}
.tile-label{position:absolute;top:2px;left:2px;font-size:4px;color:#fff}
/* tables */
table{border-collapse:collapse;width:100%}
.t-opp th{background:var(--black);color:#fff;font-size:3px;padding:1px}
.t-opp td{font-size:2.2px;line-height:2.8px;padding:1.5px 2px;height:12.5px;border-bottom:.5px solid #fff}
.t-opp tr:nth-child(odd) td{background:#ddd}
.t-opp td:first-child{font-weight:700;font-size:2.8px;width:38%}
.dot{display:inline-block;width:7px;height:7px;border-radius:50%}
.t-strat th{background:var(--black);color:#fff;font-size:1.7px;height:8px;font-weight:400}
.t-strat td{font-size:1.7px;line-height:2.2px;height:14.5px;text-align:center;padding:0 1px}
.t-strat tr:nth-child(even) td{background:#ddd}
.t-strat tr:nth-child(odd) td{background:#eee}
.t-strat td:first-child{background:#8a8a8a!important;color:#eee}
.t-ytd th{background:#333;color:#fff;font-size:1.8px;height:6px}
.t-ytd td{font-size:1.6px;height:4px;text-align:center;color:#333}
.t-ytd td:first-child{background:#8a8a8a;color:#eee;width:24%}
.t-ytd tr:nth-child(even) td:not(:first-child){background:#ddd}
/* initiatives */
.init-row{position:absolute;left:9px;width:179px;height:22px;background:#e4e4e4;border-radius:3px}
.init-tag{position:absolute;left:0;top:0;width:36px;height:22px;border-radius:3px;color:#fff;font-size:4px;line-height:5px;padding:6px 0 0 8px}
.init-list{position:absolute;left:39px;top:2px;font-size:1.7px;line-height:2.5px;color:#333}
/* core values */
.value{position:absolute;width:60px;height:48px;padding:8px 4px;color:#fff}
.value h4{font-size:4.2px;font-weight:400;margin-bottom:5px}
.value p{font-size:2.2px;line-height:3.3px}
.pill{position:absolute;width:78px;height:42px}
.pill .img{position:absolute;left:0;top:0;width:40px;height:42px}
.pill .card{position:absolute;left:38px;top:0;width:40px;height:42px;background:var(--navy);border-radius:0 0 12px 0;color:#fff;padding:4px}
.pill .card h5{font-size:2.6px;font-weight:400;margin-bottom:2px}
.pill .card p{font-size:2.1px;line-height:3.1px}
.bar-head{position:absolute;height:4px;background:var(--black);color:#fff;font-size:2.6px;line-height:4px;text-align:center}
.num-list{font-size:2.8px;line-height:4.4px;color:#222;list-style:none}
.goal{position:absolute;width:52px;text-align:center}
.goal i{display:block;margin:0 auto 2px;width:14px;height:14px;border-radius:50%;background:var(--blue);position:relative}
.goal i::after{content:"";position:absolute;left:4px;top:4px;width:6px;height:6px;border-radius:50%;border:1px solid #fff}
.goal h6{font-size:3.6px;font-weight:400;color:var(--blue)}
.goal p{font-size:1.8px;line-height:2.6px;color:#444}
.proj-col{position:absolute;width:42px}
.proj-head{height:18px;background:var(--black);color:#fff;font-size:3.6px;text-align:center;line-height:18px}
.proj-box{height:40px;font-size:1.7px;line-height:2.4px;padding:2px 3px 0 6px;color:#fff}
.proj-arrow{width:0;height:0;margin:1px auto;border-left:3px solid transparent;border-right:3px solid transparent;border-top:4px solid #000}
.proj-out{height:34px;background:#ccc;font-size:1.7px;line-height:2.4px;padding:2px 3px 0 6px;color:#333}
.fine{position:absolute;left:14px;width:170px;font-size:1.3px;color:#555}
</style>
</head>
<body>

<!-- Row 1 -->
<section class="slide" style="left:81px;top:20px">
  <div class="photo cover-photo" role="img" aria-label="Photo of a senior living building under a blue sky"></div>
  <div class="cover-band" style="left:0;top:10px;transform:rotate(-45deg)"></div>
  <div class="cover-band" style="left:10px;top:30px;transform:rotate(-45deg)"></div>
  <div class="cover-band" style="left:0;top:70px;transform:rotate(-45deg)"></div>
  <div class="cover-band" style="left:0;top:95px;transform:rotate(-135deg)"></div>
  <div class="cover-diamond"></div>
  <div class="cover-brand">VORNA</div>
  <div class="cover-title">SUPPLEMENTAL OPERATING and FINANCIAL DATA<small>SECOND QUARTER 2020</small></div>
</section>

<section class="slide" style="left:351px;top:20px">
  <h2 class="slide-title">Agenda</h2>
  <div class="brand"><span class="brand-dot"></span><span class="brand-name">VORNA</span></div>
  <div class="abs" style="left:8px;top:30px;width:84px">
    <p class="legal"><b>FORWARD-LOOKING STATEMENTS</b><br>This supplemental information contains forward-looking statements about plans, strategies, results and outlook. These statements may be identified by words such as believes, expects, may, will, should, seeks, approximately, intends, plans, estimates or anticipates. They involve known and unknown risks and uncertainties that may cause actual results to differ materially from those expressed or implied. Factors include the financial condition of our operators, changes in government reimbursement, the ability to complete acquisitions and financings, changes in interest rates, competition in the senior housing and care industry, the effects of public health events, regulatory changes and other factors described in our annual and quarterly filings. Readers are cautioned not to place undue reliance on these statements, which speak only as of the date of this report. We undertake no obligation to update or revise any forward-looking statement, whether as a result of new information, future events or otherwise, except as required by law.</p>
    <p class="legal" style="margin-top:4px"><b>NON-GAAP INFORMATION</b><br>This supplemental information contains certain non-GAAP measures, including adjusted earnings and funds from operations. Reconciliations to the most comparable GAAP measures are provided in the financial data section of this supplement.</p>
  </div>
  <div class="agenda-item" style="top:29px"><i></i>Lorem ipsum dolor sit amet, consectetur<small>Duis suscipit in tellus ac bibendum.</small></div>
  <div class="agenda-item" style="top:45px"><i></i>Lorem ipsum dolor sit amet, consectetur<small>Duis suscipit in tellus ac bibendum.</small></div>
  <div class="agenda-item" style="top:61px"><i></i>Lorem ipsum dolor sit amet, consectetur<small>Duis suscipit in tellus ac bibendum.</small></div>
  <div class="agenda-item" style="top:77px"><i></i>Lorem ipsum dolor sit amet, consectetur<small>Duis suscipit in tellus ac bibendum.</small></div>
  <div class="agenda-item" style="top:93px"><i></i>Lorem ipsum dolor sit amet, consectetur<small>Duis suscipit in tellus ac bibendum.</small></div>
  <div class="agenda-item" style="top:109px"><i></i>Lorem ipsum dolor sit amet, consectetur<small>Duis suscipit in tellus ac bibendum.</small></div>
  <div class="footer"><span>CONFIDENTIAL</span><span>Page | 2</span></div>
</section>

<section class="slide dark" style="left:621px;top:20px">
  <div class="photo about-photo" role="img" aria-label="Photo of a residential building facade"></div>
  <div class="abs" style="left:115px;top:0;width:6px;height:90px;background:var(--navy);transform:skewX(-12deg)"></div>
  <div class="abs" style="left:140px;top:0;width:5px;height:60px;background:var(--navy);transform:skewX(-12deg)"></div>
  <div class="abs" style="left:165px;top:0;width:6px;height:45px;background:var(--navy);transform:skewX(-12deg)"></div>
  <div class="abs" style="left:183px;top:0;width:4px;height:35px;background:var(--sky);transform:skewX(-12deg)"></div>
  <h2 class="about-title">ABOUT<br>VORNA</h2>
  <p class="about-tag">Here, Partners are Paramount</p>
  <div class="about-copy">
    <p>Shared success is based on partnership and alignment. Our business is about much more than real estate. It is about the operators who run the communities and the residents who call our buildings home.</p>
    <p>We focus on building strong, long-term relationships and work to align interests, ensuring that all businesses are supported to create the best outcomes for all.</p>
  </div>
</section>

<!-- Row 2 -->
<section class="slide" style="left:81px;top:188px">
  <h2 class="slide-title">About the Company</h2>
  <p class="slide-sub">Lorem ipsum, giving information on its origins, as well dummy text as a random</p>
  <div class="brand"><span class="brand-dot"></span><span class="brand-name">VORNA</span></div>
  <div class="photo" style="left:10px;top:43px;width:56px;height:52px;background:linear-gradient(180deg,#2d5ca8,#7b8aa0 55%,#4a4236)" role="img" aria-label="Building entrance at dusk"><span class="tile-label">Our Profile</span></div>
  <div class="photo" style="left:71px;top:43px;width:56px;height:52px;background:linear-gradient(180deg,#d9d2c6,#b59676 55%,#a46a3a)" role="img" aria-label="Lounge interior"><span class="tile-label">Our Mission</span></div>
  <div class="photo" style="left:132px;top:43px;width:56px;height:52px;background:linear-gradient(180deg,#3e4f62,#7c8a8e 50%,#8b6a4a)" role="img" aria-label="Therapy gym interior"><span class="tile-label">Our Vision</span></div>
  <p class="copy abs" style="left:10px;top:99px;width:56px;text-align:left"><b>Lorem Ipsum</b> is simply dummy text of the printing and typesetting industry. Lorem Ipsum has been the.</p>
  <p class="copy abs" style="left:71px;top:99px;width:56px;text-align:left"><b>Lorem Ipsum</b> is simply dummy text of the printing and typesetting industry. Lorem Ipsum has been the.</p>
  <p class="copy abs" style="left:132px;top:99px;width:56px;text-align:left"><b>Lorem Ipsum</b> is simply dummy text of the printing and typesetting industry. Lorem Ipsum has been the.</p>
  <div class="footer"><span>CONFIDENTIAL</span><span>Page | 4</span></div>
</section>

<section class="slide" style="left:351px;top:203px">
  <h2 class="slide-title">Who We Are</h2>
  <p class="slide-sub">Lorem ipsum, giving information on its origins, as well dummy text as a random</p>
  <div class="brand"><span class="brand-dot"></span><span class="brand-name">VORNA</span></div>
  <div class="photo" style="left:0;top:34px;width:67px;height:65px;background:linear-gradient(180deg,#2f5ea5,#7a8493 55%,#4b4a44)" role="img" aria-label="Building exterior"></div>
  <div class="abs" style="left:67px;top:34px;width:63px;height:65px;background:var(--navy);color:#fff;text-align:center;padding-top:24px">
    <svg width="9" height="8" viewBox="0 0 9 8" style="margin:0 auto"><path d="M1 7V5M3 7V4M5 7V3M7 7V1" stroke="#fff" stroke-width="1.2"/></svg>
    <div style="font-size:3.6px;letter-spacing:.6px;margin-top:4px">We are the Best</div>
    <div style="font-size:1.8px;line-height:2.6px;margin-top:2px"><b>Lorem Ipsum</b> is simply dummy text of the printing<br>and typesetting industry.</div>
  </div>
  <div class="photo" style="left:130px;top:34px;width:67px;height:65px;background:linear-gradient(180deg,#4b5c6e,#7f8a8d 50%,#8a6a46)" role="img" aria-label="Therapy gym with exercise balls"></div>
  <p class="copy abs" style="left:10px;top:107px;width:177px;text-align:center"><b>Lorem Ipsum</b> is simply dummy text of the printing and typesetting industry. Lorem Ipsum has been the industry's standard dummy text ever since the 1500s, when an unknown printer took a galley of type and scrambled it to make a type specimen book. It has survived not only five centuries.</p>
  <div class="footer"><span>CONFIDENTIAL</span><span>Page | 5</span></div>
</section>

<section class="slide" style="left:621px;top:188px">
  <h2 class="slide-title">Project Evaluation</h2>
  <p class="slide-sub">Lorem ipsum, giving information on its origins, as well dummy text as a random</p>
  <div class="brand"><span class="brand-dot"></span><span class="brand-name">VORNA</span></div>
  <div class="abs" style="left:9px;top:27px;width:6px;height:33px;background:var(--black);color:#fff;font-size:2px;line-height:3.2px;text-align:center;padding-top:2px">I M P A C T</div>
  <div class="abs" style="left:9px;top:98px;width:6px;height:44px;font-size:2px;line-height:3.8px;text-align:center">A C T I O N S</div>
  <div class="proj-col" style="left:20px;top:27px"><div class="proj-head">1-Lorem Impsum</div><div class="proj-box" style="background:var(--blue)">• Lorem Ipsum is simply dummy text of the printing and<br>• Lorem Ipsum is simply dummy text of the printing and</div><div class="proj-arrow"></div><div class="proj-out">• Lorem Ipsum is simply dummy text of the printing and<br>• Lorem Ipsum is simply dummy text of the printing and</div></div>
  <div class="proj-col" style="left:78px;top:27px"><div class="proj-head">2-Lorem Impsum</div><div class="proj-box" style="background:var(--sky)">• Lorem Ipsum is simply dummy text of the printing and<br>• Lorem Ipsum is simply dummy text of the printing and</div><div class="proj-arrow"></div><div class="proj-out">• Lorem Ipsum is simply dummy text of the printing and<br>• Lorem Ipsum is simply dummy text of the printing and</div></div>
  <div class="proj-col" style="left:136px;top:27px"><div class="proj-head">3-Lorem Impsum</div><div class="proj-box" style="background:#7c9cc9">• Lorem Ipsum is simply dummy text of the printing and<br>• Lorem Ipsum is simply dummy text of the printing and</div><div class="proj-arrow"></div><div class="proj-out">• Lorem Ipsum is simply dummy text of the printing and<br>• Lorem Ipsum is simply dummy text of the printing and</div></div>
  <div class="footer"><span>CONFIDENTIAL</span><span>Page | 6</span></div>
</section>

<!-- Row 3 -->
<section class="slide" style="left:81px;top:356px">
  <h2 class="slide-title">Opportunity</h2>
  <p class="slide-sub">Lorem ipsum, giving information on its origins, as well dummy text as a random</p>
  <div class="brand"><span class="brand-dot"></span><span class="brand-name">VORNA</span></div>
  <div class="abs" style="left:9px;top:27px;width:180px;border:.5px solid #999">
    <table class="t-opp">
      <tr><th>OPPORTUNITY</th><th>IMPACT</th></tr>
      <tr><td>Lorem Impsum</td><td>Lorem Ipsum is simply dummy text of the printing and Lorem Ipsum is simply dummy text of the</td></tr>
      <tr><td>Lorem Impsum</td><td>Lorem Ipsum is simply dummy text of the printing and Lorem Ipsum is simply dummy text of the</td></tr>
      <tr><td>Lorem Impsum</td><td>Lorem Ipsum is simply dummy text of the printing and Lorem Ipsum is simply dummy text of the</td></tr>
      <tr><td>Lorem Impsum</td><td>Lorem Ipsum is simply dummy text of the printing and Lorem Ipsum is simply dummy text of the</td></tr>
      <tr><td>Lorem Impsum</td><td>Lorem Ipsum is simply dummy text of the printing and Lorem Ipsum is simply dummy text of the</td></tr>
      <tr><td>Lorem Impsum</td><td>Lorem Ipsum is simply dummy text of the printing and Lorem Ipsum is simply dummy text of the</td></tr>
      <tr><td>Lorem Impsum</td><td>Lorem Ipsum is simply dummy text of the printing and Lorem Ipsum is simply dummy text of the</td></tr>
    </table>
  </div>
  <div class="footer"><span>CONFIDENTIAL</span><span>Page | 7</span></div>
</section>

<section class="slide" style="left:351px;top:355px">
  <h2 class="slide-title">Initiatives</h2>
  <p class="slide-sub">Lorem ipsum, giving information on its origins, as well dummy text as a random</p>
  <div class="brand"><span class="brand-dot"></span><span class="brand-name">VORNA</span></div>
  <div class="init-row" style="top:31px"><div class="init-tag" style="background:var(--navy)">1- Lorem<br>Impsum</div><div class="init-list">1. Lorem Ipsum is simply dummy text of the printing and typesetting industry.<br>2. Lorem Ipsum is simply dummy text of the printing and typesetting industry.<br>3. Lorem Ipsum is simply dummy text of the printing and typesetting industry.<br>4. Lorem Ipsum is simply dummy text of the printing and typesetting industry.<br>5. Lorem Ipsum is simply dummy text of the printing and typesetting industry.</div></div>
  <div class="init-row" style="top:55px"><div class="init-tag" style="background:var(--sky)">2- Lorem<br>Impsum</div><div class="init-list">1. Lorem Ipsum is simply dummy text of the printing and typesetting industry.<br>2. Lorem Ipsum is simply dummy text of the printing and typesetting industry.<br>3. Lorem Ipsum is simply dummy text of the printing and typesetting industry.<br>4. Lorem Ipsum is simply dummy text of the printing and typesetting industry.<br>5. Lorem Ipsum is simply dummy text of the printing and typesetting industry.</div></div>
  <div class="init-row" style="top:79px"><div class="init-tag" style="background:#7c8fb5">3- Lorem<br>Impsum</div><div class="init-list">1. Lorem Ipsum is simply dummy text of the printing and typesetting industry.<br>2. Lorem Ipsum is simply dummy text of the printing and typesetting industry.<br>3. Lorem Ipsum is simply dummy text of the printing and typesetting industry.<br>4. Lorem Ipsum is simply dummy text of the printing and typesetting industry.<br>5. Lorem Ipsum is simply dummy text of the printing and typesetting industry.</div></div>
  <div class="init-row" style="top:103px"><div class="init-tag" style="background:var(--pale)">4- Lorem<br>Impsum</div><div class="init-list">1. Lorem Ipsum is simply dummy text of the printing and typesetting industry.<br>2. Lorem Ipsum is simply dummy text of the printing and typesetting industry.<br>3. Lorem Ipsum is simply dummy text of the printing and typesetting industry.<br>4. Lorem Ipsum is simply dummy text of the printing and typesetting industry.<br>5. Lorem Ipsum is simply dummy text of the printing and typesetting industry.</div></div>
  <div class="footer"><span>CONFIDENTIAL</span><span>Page | 8</span></div>
</section>

<section class="slide" style="left:621px;top:356px">
  <h2 class="slide-title">Strategic Initiatives</h2>
  <p class="slide-sub">Lorem ipsum, giving information on its origins, as well dummy text as a random</p>
  <div class="brand"><span class="brand-dot"></span><span class="brand-name">VORNA</span></div>
  <div class="abs" style="left:9px;top:32px;width:180px">
    <table class="t-strat">
      <tr><th>Initiative</th><th>COVID-19 Impact</th><th>Next Steps</th><th>Timeline</th><th>Ease of Implementation</th><th>Size of Opportunity</th><th>Priority</th></tr>
      <tr><td>Lorem Ipsum</td><td>• Lorem Ipsum is simply dummy text of the printing</td><td>• Lorem ipsum is simply dummy text of the printing</td><td>1</td><td><span class="dot" style="background:var(--green)"></span></td><td>• 500k</td><td>• 5</td></tr>
      <tr><td>Lorem Ipsum</td><td>• Lorem Ipsum is simply dummy text of the printing</td><td>• Lorem Ipsum is simply dummy text of the printing</td><td>2</td><td><span class="dot" style="background:var(--green)"></span></td><td>• 200k</td><td>• 6</td></tr>
      <tr><td>Lorem Ipsum</td><td>• Lorem Ipsum is simply dummy text of the printing</td><td>• Lorem Ipsum is simply dummy text of the printing</td><td>3</td><td><span class="dot" style="background:var(--yellow)"></span></td><td>• 600k</td><td>• 4</td></tr>
      <tr><td>Lorem Ipsum</td><td>• Lorem Ipsum is simply dummy text of the printing</td><td>• Lorem Ipsum is simply dummy text of the printing</td><td>4</td><td><span class="dot" style="background:var(--amber)"></span></td><td>• 750k</td><td>• 3</td></tr>
      <tr><td>Lorem Ipsum</td><td>• Lorem Ipsum is simply dummy text of the printing</td><td>• Lorem Ipsum is simply dummy text of the printing</td><td>5</td><td><span class="dot" style="background:var(--amber)"></span></td><td>• 800k</td><td>• 2</td></tr>
      <tr><td>Lorem Ipsum</td><td>• Lorem Ipsum is simply dummy text of the printing</td><td>• Lorem Ipsum is simply dummy text of the printing</td><td>6</td><td><span class="dot" style="background:var(--red)"></span></td><td>• 900k</td><td>• 1</td></tr>
    </table>
  </div>
  <div class="footer"><span>CONFIDENTIAL</span><span>Page | 9</span></div>
</section>

<!-- Row 4 -->
<section class="slide" style="left:81px;top:524px">
  <h2 class="slide-title">Text with Picture Slide - Right</h2>
  <p class="slide-sub">Lorem ipsum, giving information on its origins, as well dummy text as a random</p>
  <div class="brand"><span class="brand-dot"></span><span class="brand-name">VORNA</span></div>
  <p class="copy abs" style="left:9px;top:32px;width:102px;font-size:1.9px;line-height:3.1px"><b>Lorem Ipsum</b> is simply dummy text of the printing and typesetting industry. Lorem Ipsum has been the industry's standard dummy text ever since the 1500s, when an unknown printer took a galley of type and scrambled it to make a type specimen book. It has survived not only five centuries, but also the leap into electronic typesetting, remaining essentially unchanged. It was popularised in the 1960s with the release of transfer sheets containing Lorem Ipsum passages, and more recently with modern publishing software including versions of Lorem Ipsum. Lorem Ipsum is simply dummy text of the printing and typesetting industry. Lorem Ipsum has been the industry's standard dummy text ever since the 1500s, when an unknown printer took a galley of type and scrambled it to make a type specimen book. It has survived not only five centuries, but also the leap into electronic typesetting, remaining essentially unchanged.</p>
  <div class="photo" style="left:118px;top:30px;width:70px;height:98px;background:linear-gradient(180deg,#4a5766,#6f7c80 45%,#8c6c48)" role="img" aria-label="Therapy gym with exercise balls and parallel bars"></div>
  <div class="footer"><span>CONFIDENTIAL</span><span>Page | 10</span></div>
</section>

<section class="slide" style="left:351px;top:512px">
  <h2 class="slide-title">Text with Picture Slide - Left</h2>
  <p class="slide-sub">Lorem ipsum, giving information on its origins, as well dummy text as a random</p>
  <div class="brand"><span class="brand-dot"></span><span class="brand-name">VORNA</span></div>
  <div class="photo" style="left:9px;top:30px;width:70px;height:98px;background:linear-gradient(180deg,#3a2a1e,#8a6a48 45%,#4d3a28)" role="img" aria-label="Dining room interior with pendant lights"></div>
  <p class="copy abs" style="left:86px;top:30px;width:102px;font-size:1.9px;line-height:3.1px">Lorem Ipsum is simply dummy text of the printing and typesetting industry. Lorem Ipsum has been the industry's standard dummy text ever since the 1500s, when an unknown printer took a galley of type and scrambled it to make a type specimen book. It has survived not only five centuries, but also the leap into electronic typesetting, remaining essentially unchanged. It was popularised in the 1960s with the release of transfer sheets containing Lorem Ipsum passages, and more recently with modern publishing software including versions of Lorem Ipsum. Lorem Ipsum is simply dummy text of the printing and typesetting industry. Lorem Ipsum has been the industry's standard dummy text ever since the 1500s, when an unknown printer took a galley of type and scrambled it to make a type specimen book. It has survived not only five centuries, but also the leap into electronic typesetting.</p>
  <div class="footer"><span>CONFIDENTIAL</span><span>Page | 11</span></div>
</section>

<section class="slide" style="left:621px;top:524px">
  <h2 class="slide-title">Company Core Values</h2>
  <p class="slide-sub">Lorem ipsum, giving information on its origins, as well dummy text as a random</p>
  <div class="brand"><span class="brand-dot"></span><span class="brand-name">VORNA</span></div>
  <div class="value" style="left:9px;top:34px;background:var(--navy)"><h4>Sample Core Values</h4><p><b>Lorem Ipsum</b> is simply dummy text of the printing and typesetting industry. Lorem Ipsum has been.</p></div>
  <div class="value" style="left:69px;top:34px;background:var(--blue)"><h4>Sample Core Values</h4><p><b>Lorem Ipsum</b> is simply dummy text of the printing and typesetting industry. Lorem Ipsum has been.</p></div>
  <div class="value" style="left:129px;top:34px;background:var(--sky)"><h4>Sample Core Values</h4><p><b>Lorem Ipsum</b> is simply dummy text of the printing and typesetting industry. Lorem Ipsum has been.</p></div>
  <div class="value" style="left:9px;top:82px;background:#5ec8ea"><h4>Sample Core Values</h4><p><b>Lorem Ipsum</b> is simply dummy text of the printing and typesetting industry. Lorem Ipsum has been.</p></div>
  <div class="value" style="left:69px;top:82px;background:#7d93d4"><h4>Sample Core Values</h4><p><b>Lorem Ipsum</b> is simply dummy text of the printing and typesetting industry. Lorem Ipsum has been.</p></div>
  <div class="value" style="left:129px;top:82px;background:var(--navy)"><h4>Sample Core Values</h4><p><b>Lorem Ipsum</b> is simply dummy text of the printing and typesetting industry. Lorem Ipsum has been.</p></div>
  <div class="footer"><span>CONFIDENTIAL</span><span>Page | 12</span></div>
</section>

<!-- Row 5 -->
<section class="slide" style="left:81px;top:692px">
  <h2 class="slide-title">Display Four Images with Text</h2>
  <p class="slide-sub">Lorem ipsum, giving information on its origins, as well dummy text as a random</p>
  <div class="brand"><span class="brand-dot"></span><span class="brand-name">VORNA</span></div>
  <div class="pill" style="left:18px;top:34px"><div class="img" style="background:linear-gradient(180deg,#cdbda6,#8b6a47)" role="img" aria-label="Lobby interior"></div><div class="card"><h5>Sample Core Values</h5><p><b>Lorem Ipsum</b> is simply dummy text of the printing and typesetting industry. Lorem Ipsum has been.</p></div></div>
  <div class="pill" style="left:102px;top:34px"><div class="img" style="background:linear-gradient(180deg,#55636f,#8a6c4a)" role="img" aria-label="Therapy gym"></div><div class="card"><h5>Sample Core Values</h5><p><b>Lorem Ipsum</b> is simply dummy text of the printing and typesetting industry. Lorem Ipsum has been.</p></div></div>
  <div class="pill" style="left:18px;top:82px"><div class="img" style="background:linear-gradient(180deg,#b9c2c9,#7b6450)" role="img" aria-label="Living room with sofas"></div><div class="card"><h5>Sample Core Values</h5><p><b>Lorem Ipsum</b> is simply dummy text of the printing and typesetting industry. Lorem Ipsum has been.</p></div></div>
  <div class="pill" style="left:102px;top:82px"><div class="img" style="background:linear-gradient(180deg,#d8d4cc,#9a8b76)" role="img" aria-label="Bright hallway interior"></div><div class="card"><h5>Sample Core Values</h5><p><b>Lorem Ipsum</b> is simply dummy text of the printing and typesetting industry. Lorem Ipsum has been.</p></div></div>
  <div class="footer"><span>CONFIDENTIAL</span><span>Page | 13</span></div>
</section>

<section class="slide" style="left:351px;top:675px">
  <h2 class="slide-title">YTD Newly Launched Products</h2>
  <p class="slide-sub" style="top:24px;font-size:3px">Lorem ipsum, giving information on its origins, as well dummy text as a random</p>
  <div class="brand"><span class="brand-dot"></span><span class="brand-name">VORNA</span></div>
  <div class="abs" style="left:9px;top:33px;width:179px">
    <table class="t-ytd">
      <tr><th>Results / New Products</th><th>APR</th><th>MAY</th><th>JUN</th><th>JUL</th><th>SEP</th><th>NOV</th><th>DIC</th></tr>
      <tr><td>Lorem Ipsum</td><td>xxx</td><td>xxx</td><td>xxx</td><td>xxx</td><td>xxx</td><td>xxx</td><td>xxx</td></tr>
      <tr><td>Lorem Ipsum</td><td>xxx</td><td>xxx</td><td>xxx</td><td>xxx</td><td>xxx</td><td>xxx</td><td>xxx</td></tr>
      <tr><td>Lorem Ipsum</td><td>xxx</td><td>xxx</td><td>xxx</td><td>xxx</td><td>xxx</td><td>xxx</td><td>xxx</td></tr>
      <tr><td>Lorem Ipsum</td><td>xxx</td><td>xxx</td><td>xxx</td><td>xxx</td><td>xxx</td><td>xxx</td><td>xxx</td></tr>
      <tr><td>Lorem Ipsum</td><td>xxx</td><td>xxx</td><td>xxx</td><td>xxx</td><td>xxx</td><td>xxx</td><td>xxx</td></tr>
      <tr><td>Lorem Ipsum</td><td>xxx</td><td>xxx</td><td>xxx</td><td>xxx</td><td>xxx</td><td>xxx</td><td>xxx</td></tr>
      <tr><td>Lorem Ipsum</td><td>xxx</td><td>xxx</td><td>xxx</td><td>xxx</td><td>xxx</td><td>xxx</td><td>xxx</td></tr>
      <tr><td>Lorem Ipsum</td><td>xxx</td><td>xxx</td><td>xxx</td><td>xxx</td><td>xxx</td><td>xxx</td><td>xxx</td></tr>
      <tr><td>Lorem Ipsum</td><td>xxx</td><td>xxx</td><td>xxx</td><td>xxx</td><td>xxx</td><td>xxx</td><td>xxx</td></tr>
      <tr><td>Lorem Ipsum</td><td>xxx</td><td>xxx</td><td>xxx</td><td>xxx</td><td>xxx</td><td>xxx</td><td>xxx</td></tr>
      <tr><td>Lorem Ipsum</td><td>xxx</td><td>xxx</td><td>xxx</td><td>xxx</td><td>xxx</td><td>xxx</td><td>xxx</td></tr>
      <tr><td>Lorem Ipsum</td><td>xxx</td><td>xxx</td><td>xxx</td><td>xxx</td><td>xxx</td><td>xxx</td><td>xxx</td></tr>
      <tr><td>Lorem Ipsum</td><td>xxx</td><td>xxx</td><td>xxx</td><td>xxx</td><td>xxx</td><td>xxx</td><td>xxx</td></tr>
      <tr><td>Lorem Ipsum</td><td>xxx</td><td>xxx</td><td>xxx</td><td>xxx</td><td>xxx</td><td>xxx</td><td>xxx</td></tr>
      <tr><td>Lorem Ipsum</td><td>xxx</td><td>xxx</td><td>xxx</td><td>xxx</td><td>xxx</td><td>xxx</td><td>xxx</td></tr>
      <tr><td>Lorem Ipsum</td><td>xxx</td><td>xxx</td><td>xxx</td><td>xxx</td><td>xxx</td><td>xxx</td><td>xxx</td></tr>
      <tr><td>Lorem Ipsum</td><td>xxx</td><td>xxx</td><td>xxx</td><td>xxx</td><td>xxx</td><td>xxx</td><td>xxx</td></tr>
      <tr><td>Lorem Ipsum</td><td>xxx</td><td>xxx</td><td>xxx</td><td>xxx</td><td>xxx</td><td>xxx</td><td>xxx</td></tr>
    </table>
  </div>
  <div class="footer"><span>CONFIDENTIAL</span><span>Page | 14</span></div>
</section>

<section class="slide" style="left:621px;top:692px">
  <h2 class="slide-title">Financial Chart</h2>
  <p class="slide-sub">Lorem ipsum, giving information on its origins, as well dummy text as a random</p>
  <div class="brand"><span class="brand-dot"></span><span class="brand-name">VORNA</span></div>
  <p class="copy abs" style="left:9px;top:34px;width:72px;font-size:1.8px;line-height:3px"><b>Lorem Ipsum</b> is simply dummy text of the printing and typesetting industry. Lorem Ipsum has been the industry's standard dummy text ever since the 1500s, when an unknown printer took a galley of type and scrambled it to make a type specimen book. It has survived not only five centuries, but also the leap into electronic typesetting, remaining essentially unchanged. It was popularised in the 1960s with the release of transfer sheets containing Lorem Ipsum passages. Lorem Ipsum is simply dummy text of the printing and typesetting industry. Lorem Ipsum has been the industry's standard dummy text ever since the 1500s, when an unknown printer took a galley of type and scrambled it to make a type specimen book.</p>
  <svg class="abs" style="left:84px;top:38px" width="106" height="82" viewBox="0 0 106 82">
    <text x="50" y="3" font-size="2.4" text-anchor="middle" fill="#333">Gross Sales ($mm)</text>
    <g stroke="#ccc" stroke-width=".3">
      <path d="M12 6V66M28 6V66M44 6V66M60 6V66M76 6V66M92 6V66"/>
    </g>
    <rect x="12" y="9" width="13" height="3" fill="var(--navy)"/>
    <rect x="12" y="12" width="16" height="3" fill="var(--blue)"/>
    <rect x="12" y="15" width="45" height="3" fill="var(--sky)"/>
    <rect x="12" y="18" width="20" height="3" fill="#7fb2e3"/>
    <rect x="12" y="21" width="11" height="3" fill="var(--pale)"/>
    <rect x="12" y="34" width="26" height="3" fill="var(--navy)"/>
    <rect x="12" y="37" width="13" height="3" fill="var(--blue)"/>
    <rect x="12" y="40" width="60" height="3" fill="var(--sky)"/>
    <rect x="12" y="43" width="36" height="3" fill="#7fb2e3"/>
    <rect x="12" y="46" width="47" height="3" fill="var(--pale)"/>
    <text x="0" y="16" font-size="1.8" fill="#333">Series One</text>
    <text x="0" y="42" font-size="1.8" fill="#333">Series Two</text>
    <g font-size="1.8" fill="#333" text-anchor="middle"><text x="12" y="70">0</text><text x="28" y="70">50</text><text x="44" y="70">100</text><text x="60" y="70">150</text><text x="76" y="70">200</text><text x="92" y="70">250</text></g>
    <text x="50" y="74" font-size="1.6" text-anchor="middle" fill="#333">■ Column 1 ■ Column 2 ■ Column 3</text>
    <text x="50" y="77" font-size="1.6" text-anchor="middle" fill="#333">■ Column 4 ■ Column 5 ■ Column 6</text>
  </svg>
  <p class="fine" style="top:133px">Lorem Ipsum is simply dummy text of the printing and typesetting industry. Lorem Ipsum has been the standard text.</p>
  <div class="footer"><span>CONFIDENTIAL</span><span>Page | 15</span></div>
</section>

<!-- Row 6 -->
<section class="slide" style="left:81px;top:860px">
  <h2 class="slide-title">Financial Smart Chart</h2>
  <p class="slide-sub">Lorem ipsum, giving information on its origins, as well dummy text as a random</p>
  <div class="brand"><span class="brand-dot"></span><span class="brand-name">VORNA</span></div>
  <svg class="abs" style="left:9px;top:32px" width="180" height="58" viewBox="0 0 180 58">
    <g font-size="2.4" fill="#333" text-anchor="end"><text x="6" y="3">50</text><text x="6" y="13">40</text><text x="6" y="23">30</text><text x="6" y="33">20</text><text x="6" y="43">10</text><text x="6" y="53">0</text></g>
    <path d="M8 52H178" stroke="#bbb" stroke-width=".4"/>
    <path d="M22 22C40 5 45 6 60 12S80 26 95 26 120 22 155 19" fill="none" stroke="#f1c232" stroke-width=".7"/>
    <path d="M22 20L60 20L95 20L130 20L155 18" fill="none" stroke="var(--sky)" stroke-width=".6"/>
    <path d="M22 27C40 35 55 38 70 38S110 33 155 24" fill="none" stroke="var(--green)" stroke-width=".6"/>
    <g fill="var(--blue)"><circle cx="22" cy="20" r=".8"/><circle cx="60" cy="20" r=".8"/><circle cx="95" cy="20" r=".8"/><circle cx="130" cy="20" r=".8"/><circle cx="155" cy="18" r=".8"/></g>
    <path d="M22 33L60 38L95 38L130 36L155 37" fill="none" stroke="var(--navy)" stroke-width=".6"/>
    <g font-size="2.4" fill="#333" text-anchor="middle"><text x="12" y="57">4/14/02</text><text x="32" y="57">5/4/02</text><text x="52" y="57">5/24/02</text><text x="72" y="57">6/13/02</text><text x="92" y="57">7/3/02</text><text x="112" y="57">7/23/02</text><text x="132" y="57">8/12/02</text><text x="152" y="57">9/1/02</text><text x="172" y="57">9/21/02</text></g>
  </svg>
  <p class="copy abs" style="left:9px;top:96px;width:180px;font-size:1.9px;line-height:3px"><b>Lorem Ipsum</b><br>is simply dummy text of the printing and typesetting industry. Lorem Ipsum has been the industry's standard dummy text ever since the 1500s, when an unknown printer took a galley of type and scrambled it to make a type specimen book. It has survived not only five centuries, but also the leap into electronic typesetting, remaining essentially unchanged. It was popularised in the 1960s with the release of transfer sheets containing Lorem Ipsum passages.</p>
  <p class="fine" style="top:133px">Lorem Ipsum is simply dummy text of the printing and typesetting industry. Lorem Ipsum has been the standard text.</p>
  <div class="footer"><span>CONFIDENTIAL</span><span>Page | 16</span></div>
</section>

<section class="slide" style="left:351px;top:848px">
  <h2 class="slide-title">Financial Smart Chart</h2>
  <p class="slide-sub">Lorem ipsum, giving information on its origins, as well dummy text as a random</p>
  <div class="brand"><span class="brand-dot"></span><span class="brand-name">VORNA</span></div>
  <svg class="abs" style="left:9px;top:32px" width="175" height="62" viewBox="0 0 175 62">
    <g font-size="2.4" fill="#333" text-anchor="end"><text x="10" y="3">50</text><text x="10" y="13">40</text><text x="10" y="23">30</text><text x="10" y="33">20</text><text x="10" y="43">10</text><text x="10" y="53">0</text></g>
    <path d="M12 52L150 52L170 40" stroke="#bbb" stroke-width=".4" fill="none"/>
    <g>
      <rect x="18" y="20" width="5" height="32" fill="var(--navy)"/><rect x="23" y="28" width="5" height="24" fill="var(--blue)"/><rect x="28" y="33" width="5" height="19" fill="var(--sky)"/><rect x="33" y="38" width="4" height="14" fill="var(--pale)"/>
      <rect x="43" y="16" width="5" height="36" fill="var(--navy)"/><rect x="48" y="23" width="5" height="29" fill="var(--blue)"/><rect x="53" y="8" width="5" height="44" fill="var(--blue)"/><rect x="58" y="38" width="4" height="14" fill="var(--pale)"/>
      <rect x="73" y="26" width="5" height="26" fill="var(--navy)"/><rect x="78" y="33" width="5" height="19" fill="var(--blue)"/><rect x="83" y="38" width="5" height="14" fill="var(--sky)"/><rect x="88" y="41" width="4" height="11" fill="var(--pale)"/>
      <rect x="103" y="24" width="5" height="28" fill="var(--navy)"/><rect x="108" y="28" width="5" height="24" fill="var(--blue)"/><rect x="113" y="33" width="5" height="19" fill="var(--sky)"/><rect x="118" y="36" width="4" height="16" fill="var(--pale)"/>
      <rect x="133" y="22" width="5" height="30" fill="var(--navy)"/><rect x="138" y="27" width="5" height="25" fill="var(--blue)"/><rect x="143" y="31" width="5" height="21" fill="var(--sky)"/><rect x="148" y="36" width="4" height="16" fill="var(--pale)"/>
    </g>
    <g font-size="2.4" fill="#333" text-anchor="middle"><text x="27" y="57">5/3/02</text><text x="55" y="59">6/1/02</text><text x="85" y="59">7/1/02</text><text x="115" y="61">8/1/02</text><text x="143" y="61">9/1/02</text></g>
  </svg>
  <p class="copy abs" style="left:9px;top:98px;width:180px;font-size:1.9px;line-height:3px"><b>Lorem Ipsum</b><br>is simply dummy text of the printing and typesetting industry. Lorem Ipsum has been the industry's standard dummy text ever since the 1500s, when an unknown printer took a galley of type and scrambled it to make a type specimen book. It has survived not only five centuries, but also the leap into electronic typesetting, remaining essentially unchanged. It was popularised in the 1960s with the release of transfer sheets containing Lorem Ipsum passages, and more recently with modern publishing software.</p>
  <div class="footer"><span>CONFIDENTIAL</span><span>Page | 17</span></div>
</section>

<section class="slide" style="left:621px;top:860px">
  <h2 class="slide-title">Financial Two Chart</h2>
  <p class="slide-sub">Lorem ipsum is simply dummy text of the printing and typesetting industry.</p>
  <div class="brand"><span class="brand-dot"></span><span class="brand-name">VORNA</span></div>
  <div class="bar-head" style="left:9px;top:27px;width:180px">Chart 1</div>
  <svg class="abs" style="left:9px;top:32px" width="180" height="48" viewBox="0 0 180 48">
    <text x="90" y="4" font-size="3.2" text-anchor="middle" fill="#555">Chart Title</text>
    <g font-size="2" fill="#555"><text x="0" y="12">6</text><text x="0" y="20">4</text><text x="0" y="28">2</text><text x="0" y="36">0</text></g>
    <path d="M5 35H178" stroke="#ccc" stroke-width=".3"/>
    <path d="M27 21L70 25L113 21L156 18" fill="none" stroke="var(--navy)" stroke-width=".6"/>
    <path d="M27 26L70 20L113 24L156 19" fill="none" stroke="var(--blue)" stroke-width=".6"/>
    <path d="M27 27L70 27L113 26L156 20" fill="none" stroke="var(--sky)" stroke-width=".6"/>
    <g font-size="2" fill="#555" text-anchor="middle"><text x="27" y="40">Category 1</text><text x="70" y="40">Category 2</text><text x="113" y="40">Category 3</text><text x="156" y="40">Category 4</text></g>
    <text x="90" y="45" font-size="1.8" text-anchor="middle" fill="#555">— Series 1 — Series 2 — Series 3</text>
  </svg>
  <div class="bar-head" style="left:9px;top:81px;width:180px">Chart 2</div>
  <svg class="abs" style="left:9px;top:86px" width="180" height="48" viewBox="0 0 180 48">
    <text x="90" y="4" font-size="3.2" text-anchor="middle" fill="#555">Chart Title</text>
    <g font-size="2" fill="#555"><text x="0" y="12">6</text><text x="0" y="20">4</text><text x="0" y="28">2</text><text x="0" y="36">0</text></g>
    <path d="M5 35H178" stroke="#ccc" stroke-width=".3"/>
    <rect x="21" y="22" width="4" height="13" fill="var(--navy)"/><rect x="26" y="27" width="4" height="8" fill="var(--blue)"/><rect x="31" y="31" width="4" height="4" fill="var(--sky)"/>
    <rect x="64" y="28" width="4" height="7" fill="var(--navy)"/><rect x="69" y="21" width="4" height="14" fill="var(--blue)"/><rect x="74" y="31" width="4" height="4" fill="var(--sky)"/>
    <rect x="107" y="24" width="4" height="11" fill="var(--navy)"/><rect x="112" y="29" width="4" height="6" fill="var(--blue)"/><rect x="117" y="25" width="4" height="10" fill="var(--sky)"/>
    <rect x="150" y="21" width="4" height="14" fill="var(--navy)"/><rect x="155" y="25" width="4" height="10" fill="var(--blue)"/><rect x="160" y="17" width="4" height="18" fill="var(--sky)"/>
    <g font-size="2" fill="#555" text-anchor="middle"><text x="27" y="40">Category 1</text><text x="70" y="40">Category 2</text><text x="113" y="40">Category 3</text><text x="156" y="40">Category 4</text></g>
    <text x="90" y="45" font-size="1.8" text-anchor="middle" fill="#555">■ Series 1 ■ Series 2 ■ Series 3</text>
  </svg>
  <div class="footer"><span>CONFIDENTIAL</span><span>Page | 18</span></div>
</section>

<!-- Row 7 -->
<section class="slide" style="left:81px;top:1028px">
  <h2 class="slide-title">Text and Two Grap</h2>
  <div class="brand"><span class="brand-dot"></span><span class="brand-name">VORNA</span></div>
  <div class="bar-head" style="left:9px;top:26px;width:180px">Lorem lorem</div>
  <ol class="num-list abs" style="left:11px;top:31px">
    <li>1. Lorem ipsum is simply dummy text of the printing and typesetting industry.</li>
    <li>2. Lorem ipsum is simply dummy text of the printing and typesetting industry.</li>
    <li>3. Lorem ipsum is simply dummy text of the printing and typesetting industry.</li>
    <li>4. Lorem ipsum is simply dummy text of the printing and typesetting industry.</li>
    <li>5. Lorem ipsum is simply dummy text of the printing and typesetting industry.</li>
  </ol>
  <div class="bar-head" style="left:9px;top:81px;width:87px">Lorem loren</div>
  <div class="bar-head" style="left:102px;top:81px;width:87px">Lorem loren</div>
  <svg class="abs" style="left:9px;top:87px" width="87" height="40" viewBox="0 0 87 40">
    <path d="M6 36H70" stroke="#bbb" stroke-width=".3"/>
    <rect x="12" y="22" width="7" height="14" fill="var(--navy)"/><rect x="12" y="18" width="7" height="4" fill="var(--blue)"/>
    <rect x="27" y="20" width="7" height="16" fill="var(--navy)"/><rect x="27" y="16" width="7" height="4" fill="var(--blue)"/>
    <rect x="42" y="22" width="7" height="14" fill="var(--navy)"/><rect x="42" y="18" width="7" height="4" fill="var(--blue)"/>
    <rect x="57" y="16" width="7" height="20" fill="var(--navy)"/><rect x="57" y="8" width="7" height="8" fill="var(--sky)"/>
    <g font-size="1.6" fill="#555"><text x="73" y="18">■ Serie 3</text><text x="73" y="22">■ Serie 2</text><text x="73" y="26">■ Serie 1</text></g>
    <g font-size="1.6" fill="#555" text-anchor="middle"><text x="15" y="39.5">Cat 1</text><text x="30" y="39.5">Cat 2</text><text x="45" y="39.5">Cat 3</text><text x="60" y="39.5">Cat 4</text></g>
  </svg>
  <svg class="abs" style="left:102px;top:87px" width="87" height="40" viewBox="0 0 87 40">
    <path d="M6 36H70" stroke="#bbb" stroke-width=".3"/>
    <path d="M12 22L27 28L42 18L60 12" fill="none" stroke="var(--sky)" stroke-width=".6"/>
    <path d="M12 14L27 26L42 24L60 20" fill="none" stroke="#f1c232" stroke-width=".6"/>
    <path d="M12 28L27 18L42 26L60 16" fill="none" stroke="var(--red)" stroke-width=".6"/>
    <path d="M12 24L27 22L42 30L60 22" fill="none" stroke="var(--green)" stroke-width=".6"/>
    <g font-size="1.6" fill="#555"><text x="73" y="18">— Serie 1</text><text x="73" y="22">— Serie 2</text><text x="73" y="26">— Serie 3</text></g>
    <g font-size="1.6" fill="#555" text-anchor="middle"><text x="12" y="39.5">Cat 1</text><text x="27" y="39.5">Cat 2</text><text x="42" y="39.5">Cat 3</text><text x="60" y="39.5">Cat 4</text></g>
  </svg>
  <p class="fine" style="top:134px">Lorem Ipsum is simply dummy text of the printing and typesetting industry. Lorem Ipsum has been the standard text.</p>
  <div class="footer"><span>CONFIDENTIAL</span><span>Page | 19</span></div>
</section>

<section class="slide" style="left:351px;top:1028px">
  <h2 class="slide-title">Text and Two Grap</h2>
  <p class="slide-sub">Lorem ipsum, giving information on its origins, as well dummy text as a random</p>
  <div class="brand"><span class="brand-dot"></span><span class="brand-name">VORNA</span></div>
  <div class="bar-head" style="left:9px;top:26px;width:87px">Loren loren</div>
  <div class="bar-head" style="left:102px;top:26px;width:87px">Loren loren</div>
  <svg class="abs" style="left:9px;top:31px" width="87" height="42" viewBox="0 0 87 42">
    <g font-size="1.6" fill="#555" text-anchor="end"><text x="6" y="4">100%</text><text x="6" y="11">80%</text><text x="6" y="18">60%</text><text x="6" y="25">40%</text><text x="6" y="32">20%</text><text x="6" y="39">0%</text></g>
    <path d="M8 38H72" stroke="#bbb" stroke-width=".3"/>
    <path d="M14 10L30 10L48 12L64 14" fill="none" stroke="#9bbb59" stroke-width=".6"/>
    <path d="M14 16L30 17L48 18L64 19" fill="none" stroke="var(--navy)" stroke-width=".6"/>
    <path d="M14 22L30 28L48 21L64 24" fill="none" stroke="var(--sky)" stroke-width=".6"/>
    <g font-size="1.6" fill="#555"><text x="74" y="16">— Serie 3</text><text x="74" y="20">— Serie 2</text><text x="74" y="24">— Serie 1</text></g>
    <g font-size="1.6" fill="#555" text-anchor="middle"><text x="14" y="41.5">Cat 1</text><text x="30" y="41.5">Cat 2</text><text x="48" y="41.5">Cat 3</text><text x="64" y="41.5">Cat 4</text></g>
  </svg>
  <svg class="abs" style="left:102px;top:31px" width="87" height="42" viewBox="0 0 87 42">
    <g font-size="1.6" fill="#555" text-anchor="end"><text x="6" y="4">14</text><text x="6" y="9">12</text><text x="6" y="14">10</text><text x="6" y="19">8</text><text x="6" y="24">6</text><text x="6" y="29">4</text><text x="6" y="34">2</text><text x="6" y="39">0</text></g>
    <path d="M8 38H72" stroke="#bbb" stroke-width=".3"/>
    <path d="M14 16L30 16L48 16L64 8" fill="none" stroke="var(--sky)" stroke-width=".6"/>
    <path d="M14 22L30 20L48 24L64 18" fill="none" stroke="var(--navy)" stroke-width=".6"/>
    <path d="M14 26L30 27L48 26L64 24" fill="none" stroke="#9bbb59" stroke-width=".6"/>
    <g font-size="1.6" fill="#555"><text x="74" y="16">— Serie 3</text><text x="74" y="20">— Serie 2</text><text x="74" y="24">— Serie 1</text></g>
    <g font-size="1.6" fill="#555" text-anchor="middle"><text x="14" y="41.5">Cat 1</text><text x="30" y="41.5">Cat 2</text><text x="48" y="41.5">Cat 3</text><text x="64" y="41.5">Cat 4</text></g>
  </svg>
  <div class="bar-head" style="left:9px;top:76px;width:180px">Loren loren</div>
  <ol class="abs" style="left:11px;top:82px;list-style:none;color:#222">
    <li style="font-size:2.8px;line-height:4.2px">1. Lorem Ipsum is simply dummy text of the printing and typesetting industry.</li>
    <li style="font-size:2.5px;line-height:4px;padding-left:2px">1. Lorem Ipsum is simply dummy text of the printing and typesetting industry.</li>
    <li style="font-size:2.2px;line-height:3.8px;padding-left:4px">1. Lorem Ipsum is simply dummy text of the printing and typesetting industry.</li>
    <li style="font-size:1.9px;line-height:3.6px;padding-left:6px">1. Lorem Ipsum is simply dummy text of the printing and typesetting industry.</li>
    <li style="font-size:1.6px;line-height:3.4px;padding-left:8px">1. Lorem Ipsum is simply dummy text of the printing and typesetting industry.</li>
  </ol>
  <p class="fine" style="top:134px">Lorem Ipsum is simply dummy text of the printing and typesetting industry. Lorem Ipsum has been the standard text.</p>
  <div class="footer"><span>CONFIDENTIAL</span><span>Page | 20</span></div>
</section>

<section class="slide" style="left:621px;top:1028px">
  <h2 class="slide-title">Goals</h2>
  <p class="abs" style="left:11px;top:24px;font-size:2.9px;color:#333;text-transform:uppercase">Lorem ipsum, giving information on its origins, as well dummy text as a random</p>
  <div class="brand"><span class="brand-dot"></span><span class="brand-name">VORNA</span></div>
  <div class="goal" style="left:14px;top:40px"><i style="background:var(--navy)"></i><h6>Photo</h6><p><b>Lorem Ipsum</b> is simply dummy text of the printing and typesetting industry.</p></div>
  <div class="goal" style="left:73px;top:40px"><i></i><h6>Support</h6><p><b>Lorem Ipsum</b> is simply dummy text of the printing and typesetting industry.</p></div>
  <div class="goal" style="left:132px;top:40px"><i style="background:var(--sky)"></i><h6>Desing</h6><p><b>Lorem Ipsum</b> is simply dummy text of the printing and typesetting industry.</p></div>
  <div class="goal" style="left:14px;top:80px"><i style="background:var(--sky)"></i><h6>Audio</h6><p><b>Lorem Ipsum</b> is simply dummy text of the printing and typesetting industry.</p></div>
  <div class="goal" style="left:73px;top:80px"><i style="background:#3d6fb3"></i><h6>SEO</h6><p><b>Lorem Ipsum</b> is simply dummy text of the printing and typesetting industry.</p></div>
  <div class="goal" style="left:132px;top:80px"><i style="background:var(--pale)"></i><h6>Desing</h6><p><b>Lorem Ipsum</b> is simply dummy text of the printing and typesetting industry.</p></div>
  <div class="footer"><span>CONFIDENTIAL</span><span>Page | 21</span></div>
</section>

</body>
</html>
```